Business Card for a mobile physiotherapy company

I need a layout for a business card for a mobile physiotherapy company.
Slogan is "Mobile Physiotherapy - Your Road To Recovery"
Phone number is 867-412-5093
Email VantePhysio@mailbox-demo.ca (subject to change with website)
Website www.VantePhysio.ca
My name and credentials: Gil Varney Gil Varney, BSc(kin), MPT, CAFCI, IMS
Information maybe included: Direct Billing, Services including Physiotherapy, IMS, acupuncture
Maybe include facebook and instagram logos
One side with the logo clean and sharp
Other side with details, try not to look too busy, keep everything concise

```html
<!DOCTYPE html>
<html lang="en">
<head>
<meta charset="utf-8">
<title>Vante Therapy – Business Card</title>
<link href="https://fonts.googleapis.com/css2?family=Tinos:ital,wght@0,400;0,700;1,400&display=swap" rel="stylesheet">
<style>
  :root {
    --navy: #2c4a73;
    --navy-dark: #283f63;
    --green: #1d5a48;
    --band-green: #175c4a;
    --ink: #3c4a66;
    --paper: #ffffff;
    --paper-shade: #eceef2;
    --backdrop: #e4e1dc;
  }
  * { box-sizing: border-box; margin: 0; padding: 0; }
  html, body {
    width: 900px; height: 1200px; overflow: hidden;
    background: var(--backdrop);
    font-family: "Tinos", "Times New Roman", serif;
  }
  .card {
    position: absolute; left: 80px; width: 732px; height: 428px;
    border-radius: 22px; overflow: hidden;
    box-shadow: 0 4px 10px rgba(0,0,0,0.25);
  }
  .card-front {
    top: 130px;
    background: linear-gradient(120deg, var(--paper) 55%, var(--paper-shade) 100%);
  }
  .card-back { top: 645px; background: var(--navy); }

  .holder-name {
    position: absolute; left: 48px; top: 70px;
    font-size: 28px; font-weight: 700; letter-spacing: 1px;
    color: var(--green); text-transform: uppercase;
  }
  .holder-credentials {
    position: absolute; left: 48px; top: 106px;
    font-size: 19px; color: var(--ink);
  }

  .brand {
    position: absolute; font-size: 44px; font-weight: 700; line-height: 1.1;
  }
  .brand-front { right: 46px; top: 150px; width: 240px; text-align: center; color: var(--green); }
  .brand-back { left: 0; right: 0; top: 215px; text-align: center; color: var(--paper); }

  .divider {
    position: absolute; left: 48px; right: 46px; top: 308px;
    border-top: 2px solid var(--navy);
  }
  .contact-row {
    position: absolute; left: 46px; right: 46px; top: 322px;
    display: flex; justify-content: space-between; list-style: none;
  }
  .contact-item {
    display: flex; align-items: center; gap: 9px;
    font-size: 17px; color: var(--green);
  }
  .contact-icon { width: 23px; height: 23px; }

  .info-band {
    position: absolute; left: 0; right: 0; top: 390px; height: 22px;
    background: var(--band-green); color: var(--paper); font-size: 15px;
  }
  .billing { position: absolute; left: 47px; top: 2px; }
  .services {
    position: absolute; left: 187px; width: 418px; top: -4px; height: 26px;
    background: var(--navy-dark);
    clip-path: polygon(0 0, 100% 0, 96% 100%, 4% 100%);
    display: flex; align-items: center; justify-content: center; gap: 10px;
  }
  .services strong { font-weight: 700; }
  .social { position: absolute; right: 44px; top: 3px; display: flex; gap: 8px; }
  .social span { width: 16px; height: 16px; border-radius: 3px; background: var(--paper); }

  .slogan {
    position: absolute; left: 0; right: 0; top: 364px; text-align: center;
    font-style: italic; font-size: 18px; color: var(--paper);
  }
</style>
</head>
<body>
  <section class="card card-front" aria-label="Card front">
    <h1 class="holder-name">Gil Varney</h1>
    <p class="holder-credentials">BSc(kin), MPT, CAFCI, IMS</p>

    <p class="brand brand-front">Vante<br>Therapy</p>

    <div class="divider"></div>
    <ul class="contact-row">
      <li class="contact-item">
        <svg class="contact-icon" viewBox="0 0 24 24"><circle cx="12" cy="12" r="12" fill="#2c4a73"/><path d="M8 6.5c.6-.4 1.2-.3 1.5.2l1.2 2c.3.5.1 1-.3 1.3l-.7.5c.6 1.4 1.6 2.4 3 3l.5-.7c.3-.4.9-.6 1.3-.3l2 1.2c.5.3.6.9.2 1.5-.8 1.1-2 1.6-3.3 1-2.9-1.2-4.9-3.2-6.1-6.1-.5-1.3 0-2.5 1-3.3z" fill="#fff"/></svg>
        867-412-5093
      </li>
      <li class="contact-item">
        <svg class="contact-icon" viewBox="0 0 24 24"><circle cx="12" cy="12" r="12" fill="#2c4a73"/><rect x="6.5" y="8" width="11" height="8" fill="#fff"/><path d="M6.5 8l5.5 4.5L17.5 8" fill="none" stroke="#2c4a73" stroke-width="1.2"/></svg>
        VantePhysio@mailbox-demo.ca
      </li>
      <li class="contact-item">
        <svg class="contact-icon" viewBox="0 0 24 24"><circle cx="12" cy="12" r="12" fill="#2c4a73"/><g fill="none" stroke="#fff" stroke-width="1.1"><circle cx="12" cy="12" r="6"/><ellipse cx="12" cy="12" rx="2.6" ry="6"/><path d="M6 12h12M7 9h10M7 15h10"/></g></svg>
        www.VantePhysio.ca
      </li>
    </ul>

    <div class="info-band">
      <span class="billing">Direct Billing</span>
      <div class="services">
        <strong>Services</strong><span>›</span><span>Physiotherapy</span><span>•</span><span>IMS</span><span>•</span><span>Acupuncture</span>
      </div>
      <div class="social" role="img" aria-label="Social media links"><span></span><span></span></div>
    </div>
  </section>

  <section class="card card-back" aria-label="Card back">
    <p class="brand brand-back">Vante<br>Therapy</p>
    <p class="slogan">Mobile Physiotherapy - Your Road To Recovery</p>
  </section>
</body>
</html>
```